Fun Trendy High End Spa Services
Business Card, Gift Certificate, Gift Certificate Envelope
I need double sided standard sized Business Card [3.5" x 2"]
We like what is in logo that was uploaded but please use your creativity. We are open to any ideas.
Simple
Lena Harbus LMT
Owner
Mobile
BP@BrightPebblo.com
BrightPebblo.com
We are open to all concepts. So please be creative. This is for Very high end spa service so it needs to look very good. We thought black paper for a base on business cards, gift certificate and GC envelope but are open to any and all ideas! Thank You! We will pick a winner early if we find the perfect design.
"The greatest wealth is health"
(Doesnt need " " on there just use your own idea and play with it.)
Here is The winning logo design. We really like the style but please feel free to be creative with it! Thank you so much!
This is the style of gift certificate that we want designed to match our business card.

```html
<!DOCTYPE html>
<html lang="en">
<head>
<meta charset="utf-8">
<title>Bright Pebblo – Stationery Set</title>
<link href="https://fonts.googleapis.com/css2?family=Comfortaa:wght@400&family=Great+Vibes&family=Open+Sans:ital,wght@0,400;0,600;1,400;1,600&display=swap" rel="stylesheet">
<style>
  :root {
    --ink: #141414;
    --paper: #f4f4f4;
    --paper-shade: #dcdcdc;
    --silver: #b9b9b9;
    --pink: #e0207a;
    --text: #333333;
    --muted: #8a8a8a;
    --canvas: #ebe7e1;
  }
  * { box-sizing: border-box; margin: 0; padding: 0; }
  html, body { width: 1200px; height: 887px; overflow: hidden; }
  body { background: var(--canvas); font-family: "Open Sans", sans-serif; position: relative; }

  .piece { position: absolute; overflow: hidden; box-shadow: 0 3px 10px rgba(0,0,0,.25); }
  .piece > svg.art { position: absolute; inset: 0; width: 100%; height: 100%; }

  .brand { position: absolute; display: flex; align-items: center; gap: 8px; color: #fff; }
  .brand-dot { border: 2px solid #fff; border-radius: 50%; flex: none; }
  .brand-name { font-family: "Comfortaa", sans-serif; font-weight: 400; line-height: 1.05; }
  .brand-tagline { position: absolute; color: var(--pink); font-size: 10px; }

  /* Gift certificate */
  .certificate { left: 101px; top: 101px; width: 571px; height: 307px;
    background: linear-gradient(160deg, #ffffff 30%, var(--paper) 60%, var(--paper-shade)); }
  .certificate .brand { left: 24px; top: 16px; }
  .certificate .brand-dot { width: 34px; height: 34px; }
  .certificate .brand-name { font-size: 23px; }
  .certificate .brand-tagline { left: 24px; top: 76px; }
  .certificate-title { position: absolute; right: 18px; top: 10px; font-family: "Great Vibes", cursive; font-size: 38px; color: var(--text); }
  .certificate-meta { position: absolute; right: 70px; top: 66px; font-size: 10px; color: var(--text); word-spacing: 4px; }
  .certificate-fields { position: absolute; left: 36px; top: 120px; width: 340px; list-style: none; }
  .certificate-fields li { display: flex; align-items: flex-end; gap: 6px; height: 38px; font-size: 13px; font-style: italic; color: var(--text); }
  .certificate-fields li span.line { flex: 1; border-bottom: 1.5px dotted var(--muted); margin-bottom: 4px; }
  .quote { font-style: italic; font-weight: 600; color: var(--pink); }
  .certificate .quote { position: absolute; left: 0; right: 0; bottom: 8px; text-align: center; font-size: 12px; }

  /* Envelope */
  .envelope { left: 101px; top: 420px; width: 571px; height: 372px;
    background: linear-gradient(180deg, #ffffff, var(--paper) 70%, var(--paper-shade)); }
  .envelope .flap-dot { position: absolute; left: 270px; top: 14px; width: 30px; height: 30px; border-radius: 50%; border: 2px solid var(--ink); }
  .envelope .brand { left: 28px; top: 120px; }
  .envelope .brand-dot { width: 30px; height: 30px; }
  .envelope .brand-name { font-size: 21px; }
  .envelope .brand-tagline { left: 28px; top: 176px; }
  .contact-strip { position: absolute; right: 36px; bottom: 10px; display: flex; gap: 18px; font-size: 10px; font-weight: 600; font-style: italic; color: #fff; }
  .contact-strip b, .contact b { color: var(--pink); font-style: normal; margin-right: 3px; }

  /* Business cards */
  .card { width: 379px; height: 224px; background: var(--ink); }
  .card-front { left: 720px; top: 180px; }
  .card-back { left: 720px; top: 444px; }
  .card-front .brand { left: 24px; top: 20px; }
  .card-front .brand-dot { width: 34px; height: 34px; }
  .card-front .brand-name { font-size: 23px; }
  .card-front .brand-tagline { left: 66px; top: 86px; color: #fff; font-size: 11px; }
  .holder { position: absolute; left: 18px; top: 164px; color: var(--text); }
  .holder-name { font-size: 15px; font-weight: 600; color: var(--pink); }
  .holder-name small { font-size: 10px; color: var(--text); }
  .holder-role { font-size: 10px; }
  .contact { position: absolute; right: 14px; top: 176px; font-size: 10px; line-height: 1.5; color: var(--text); }
  .back-mark { position: absolute; left: 164px; top: 30px; width: 54px; height: 54px; border-radius: 50%; border: 3px solid var(--silver); }
  .card-back .quote { position: absolute; right: 16px; top: 170px; font-size: 11px; color: var(--text); font-weight: 400; text-align: right; line-height: 1.5; }
  .card-back .quote span { display: block; color: var(--pink); font-size: 9px; font-weight: 600; }
</style>
</head>
<body>

<section class="piece certificate" aria-label="Gift certificate">
  <svg class="art" viewBox="0 0 571 307" preserveAspectRatio="none" aria-hidden="true">
    <path d="M0 0 H330 C250 14 160 70 0 108 Z" fill="var(--ink)"/>
    <path d="M0 112 C160 74 250 20 340 0" fill="none" stroke="var(--silver)" stroke-width="5"/>
    <circle cx="430" cy="160" r="70" fill="none" stroke="#e6e6e6" stroke-width="6"/>
    <rect x="0" y="277" width="571" height="30" fill="var(--ink)"/>
  </svg>
  <div class="brand"><span class="brand-dot"></span><span class="brand-name">Bright<br>Pebblo</span></div>
  <p class="brand-tagline">Luxury In Home Spa Experience</p>
  <h1 class="certificate-title">Gift Certificate</h1>
  <p class="certificate-meta">No. 123456789 Date. 11-22-3333</p>
  <ul class="certificate-fields">
    <li>In the Amount of <span class="line"></span></li>
    <li>A Gift for <span class="line"></span></li>
    <li>Presented By <span class="line"></span></li>
  </ul>
  <p class="quote">"The greatest wealth is health"</p>
</section>

<section class="piece envelope" aria-label="Gift certificate envelope">
  <svg class="art" viewBox="0 0 571 372" preserveAspectRatio="none" aria-hidden="true">
    <path d="M0 0 H571 V60 C420 96 150 96 0 60 Z" fill="#ffffff"/>
    <path d="M0 60 C150 96 420 96 571 60" fill="none" stroke="var(--paper-shade)" stroke-width="2"/>
    <path d="M0 108 H300 C240 150 160 180 0 212 Z" fill="var(--ink)"/>
    <path d="M0 218 C160 186 250 150 320 108" fill="none" stroke="var(--silver)" stroke-width="5"/>
    <circle cx="300" cy="260" r="78" fill="none" stroke="#e6e6e6" stroke-width="6"/>
    <rect x="0" y="340" width="571" height="32" fill="var(--ink)"/>
  </svg>
  <span class="flap-dot" aria-hidden="true"></span>
  <div class="brand"><span class="brand-dot"></span><span class="brand-name">Bright<br>Pebblo</span></div>
  <p class="brand-tagline">Luxury In Home Spa Experience</p>
  <p class="contact-strip"><span><b>p.</b>555-013-2741</span><span><b>w.</b>BrightPebblo.com</span></p>
</section>

<section class="piece card card-front" aria-label="Business card front">
  <svg class="art" viewBox="0 0 379 224" preserveAspectRatio="none" aria-hidden="true">
    <path d="M0 224 V150 C140 150 300 130 379 60 V224 Z" fill="var(--paper)"/>
    <path d="M0 142 C150 142 300 122 379 50" fill="none" stroke="var(--silver)" stroke-width="6"/>
  </svg>
  <div class="brand"><span class="brand-dot"></span><span class="brand-name">Bright<br>Pebblo</span></div>
  <p class="brand-tagline">Luxury In Home Spa Experience</p>
  <div class="holder">
    <p class="holder-name">LENA HARBUS <small>LMT</small></p>
    <p class="holder-role">Owner</p>
  </div>
  <p class="contact"><b>p.</b>555-013-2741<br><b>w.</b>BrightPebblo.com</p>
</section>

<section class="piece card card-back" aria-label="Business card back">
  <svg class="art" viewBox="0 0 379 224" preserveAspectRatio="none" aria-hidden="true">
    <path d="M0 224 V196 C140 190 300 150 379 80 V224 Z" fill="var(--paper)"/>
    <path d="M0 188 C150 182 300 140 379 70" fill="none" stroke="var(--silver)" stroke-width="6"/>
  </svg>
  <span class="back-mark" aria-hidden="true"></span>
  <p class="quote">"The greatest wealth is health"<span>www.BrightPebblo.com</span></p>
</section>

</body>
</html>
```